Delcourt Realty Business Cards

Design business card

Target Market(s)

High-End Buyer of Real Estate over $1 million dollars

Industry/Entity Type

Realtor

Contact Information for Business Card

Lena Delcourt R(S) LIC.# 41972
Cell 555 246-1938
Email Lena@Delcourt.example
Website IsleFreshHomes.example

Also Need Cards for:

Hank Delcourt R(B) LIC# 69418
C 555 613-7052
E Hank@Delcourt.example
W IsleFreshHomes.example

Colors

Designer to choose colors to be used in the design.

Requirements
Must have
• Address on back:
• 287 Pohaku Cir. , Wailea HI 96753
• Logo on back
Nice to have
• I would like the phone numbers and email address to be big so people can read it easily
Should not have
• Very small print Except For: address (287 Pohaku Cir. Wailea HI 96753)

```html
<!DOCTYPE html>
<html lang="en">
<head>
<meta charset="utf-8">
<title>Delcourt Realty Business Cards</title>
<link href="https://fonts.googleapis.com/css2?family=Crimson+Text:wght@600&display=swap" rel="stylesheet">
<style>
  :root {
    --card: #59595b;
    --ink: #0e0e0e;
    --gap: #ffffff;
    --strip: #d9d9d9;
  }
  html, body {
    margin: 0;
    padding: 0;
    width: 985px;
    height: 1200px;
    overflow: hidden;
    background: var(--gap);
  }
  .sheet {
    position: relative;
    width: 985px;
    height: 1200px;
    font-family: "Crimson Text", "Palatino Linotype", Georgia, serif;
    font-weight: 600;
    color: var(--ink);
  }
  .card {
    position: absolute;
    left: 0;
    width: 985px;
    background: var(--card);
    overflow: hidden;
  }
  .card-front { top: 0; height: 588px; }
  .card-back { top: 595px; height: 591px; }
  .bottom-strip {
    position: absolute;
    left: 0;
    top: 1186px;
    width: 985px;
    height: 14px;
    background: var(--strip);
  }
  .brand-square {
    position: absolute;
    background: var(--ink);
  }
  .brand-name {
    position: absolute;
    margin: 0;
    line-height: 1;
    color: var(--ink);
    font-weight: 600;
    white-space: nowrap;
  }
  .front-square { left: 116px; top: 172px; width: 247px; height: 247px; }
  .front-name { left: 398px; top: 205px; font-size: 92px; }
  .back-square { left: 68px; top: 62px; width: 110px; height: 110px; }
  .back-name { left: 68px; top: 188px; font-size: 46px; }
  .agent-name, .contact-line, .office-line {
    position: absolute;
    margin: 0;
    line-height: 1;
    white-space: nowrap;
  }
  .agent-name { font-size: 30px; left: 462px; }
  .contact-line { font-size: 37px; left: 524px; }
  .office-line { left: 142px; font-size: 29px; }
  .icon { position: absolute; }
  .divider {
    position: absolute;
    left: 497px;
    width: 5px;
    border-radius: 3px;
    background: var(--ink);
  }
</style>
</head>
<body>
<div class="sheet">
  <section class="card card-front">
    <div class="brand-square front-square"></div>
    <p class="brand-name front-name">Delcourt<br>Realty</p>
  </section>

  <section class="card card-back">
    <div class="brand-square back-square"></div>
    <p class="brand-name back-name">Delcourt<br>Realty</p>
  </section>

  <!-- agent one -->
  <p class="agent-name" style="top:662px">Lena Delcourt R(S) LIC.# 41972</p>
  <svg class="icon" style="left:405px;top:711px" width="79" height="51" viewBox="0 0 79 51">
    <rect width="79" height="51" fill="var(--ink)"/>
    <polyline points="3,4 39.5,32 76,4" fill="none" stroke="var(--card)" stroke-width="4"/>
  </svg>
  <div class="divider" style="top:707px;height:120px"></div>
  <p class="contact-line" style="top:712px">Lena@Delcourt.example</p>
  <svg class="icon" style="left:421px;top:775px" width="52" height="52" viewBox="0 0 52 52">
    <circle cx="26" cy="26" r="23" fill="none" stroke="var(--ink)" stroke-width="3.5"/>
    <path d="M18 14c2-1 4 0 5 2l2 4c0 2-1 3-2 4 1 3 3 5 6 6 1-1 2-2 4-2l4 2c2 1 3 3 2 5-1 2-3 3-6 3-9-1-16-8-17-17 0-3 1-6 2-7z" fill="var(--ink)"/>
  </svg>
  <p class="contact-line" style="top:784px">555 246-1938</p>

  <!-- agent two -->
  <p class="agent-name" style="top:848px">Hank Delcourt R(B) LIC# 69418</p>
  <svg class="icon" style="left:405px;top:897px" width="79" height="51" viewBox="0 0 79 51">
    <rect width="79" height="51" fill="var(--ink)"/>
    <polyline points="3,4 39.5,32 76,4" fill="none" stroke="var(--card)" stroke-width="4"/>
  </svg>
  <div class="divider" style="top:895px;height:118px"></div>
  <p class="contact-line" style="top:898px">Hank@Delcourt.example</p>
  <svg class="icon" style="left:421px;top:961px" width="52" height="52" viewBox="0 0 52 52">
    <circle cx="26" cy="26" r="23" fill="none" stroke="var(--ink)" stroke-width="3.5"/>
    <path d="M18 14c2-1 4 0 5 2l2 4c0 2-1 3-2 4 1 3 3 5 6 6 1-1 2-2 4-2l4 2c2 1 3 3 2 5-1 2-3 3-6 3-9-1-16-8-17-17 0-3 1-6 2-7z" fill="var(--ink)"/>
  </svg>
  <p class="contact-line" style="top:969px">555 613-7052</p>

  <!-- office -->
  <svg class="icon" style="left:80px;top:1020px" width="44" height="44" viewBox="0 0 44 44">
    <g fill="none" stroke="var(--ink)" stroke-width="2.5">
      <circle cx="22" cy="22" r="19"/>
      <ellipse cx="22" cy="22" rx="8" ry="19"/>
      <line x1="3" y1="22" x2="41" y2="22"/>
      <line x1="22" y1="3" x2="22" y2="41"/>
      <path d="M6 12h32M6 32h32"/>
    </g>
  </svg>
  <p class="office-line" style="top:1027px">IsleFreshHomes.example</p>
  <svg class="icon" style="left:87px;top:1074px" width="30" height="42" viewBox="0 0 30 42">
    <path d="M15 1C7 1 1 7 1 15c0 10 14 26 14 26s14-16 14-26C29 7 23 1 15 1z" fill="var(--ink)"/>
    <circle cx="15" cy="15" r="6" fill="var(--card)"/>
  </svg>
  <p class="office-line" style="top:1083px">287 Pohaku Cir. , Wailea HI 96753</p>

  <div class="bottom-strip" role="img" aria-label="Decorative star pattern border"></div>
</div>
</body>
</html>
```